card design for engineering consultancy

engineering drafting and project management company the provides drafting services for.
Electrical, Hydraulic, Mechanical, and Civil services
The company is called Q7R Services and logo is as attached
Information on card should be.
1. Logo
2.website : Q7RServices.example
3. email : info@Q7RServices.example
4. Phone: (+61) 400512836
5. Motto: Design - Document - Develop - Deliver

this card should be basically used for business identification only

Target Market(s)

electricians plumbers air conditioning installers and civil contractors

Industry/Entity Type

engineering, drafting, electrical, plumbing, airconditioning, civil

Contact Information for Business Card

1. Logo 2.website : Q7RServices.example 3. email : info@Q7RServices.example 4. Phone: (+61) 400512836 5. Motto: Design - Document - Develop - Deliver

Font styles to use
Serif

Requirements
Must have
• logo
Nice to have
• something inovative and different that makes it stand out from being just another business card

```html
<!DOCTYPE html>
<html lang="en">
<head>
<meta charset="utf-8">
<title>Q7R Services – Business Card</title>
<link href="https://fonts.googleapis.com/css2?family=Exo+2:wght@400;600;700&display=swap" rel="stylesheet">
<style>
  :root {
    --backdrop: #2b2b2d;
    --card: #111013;
    --card-edge: #1c1b1e;
    --text-grey: #5c5c5f;
    --logo-grey: #58585b;
    --accent-red: #e8262a;
    --rule: #3a3a3d;
    --wave-tone: #1f1e23;
  }
  * { margin: 0; padding: 0; box-sizing: border-box; }
  html, body {
    width: 1200px; height: 1000px; overflow: hidden;
    background: var(--backdrop);
    font-family: "Exo 2", sans-serif;
  }
  .canvas { position: relative; width: 1200px; height: 1000px; }

  .card {
    position: absolute;
    background: var(--card);
    border: 1px solid var(--card-edge);
    border-radius: 44px;
    overflow: hidden;
  }
  .card--front { left: 125px; top: 102px; width: 732px; height: 408px; }
  .card--back  { left: 293px; top: 533px; width: 726px; height: 405px; }

  .wave-field { position: absolute; }
  .card--front .wave-field {
    right: 0; top: 0; width: 460px; height: 260px;
    background: radial-gradient(ellipse at 80% 25%, var(--wave-tone), transparent 70%);
  }
  .card--back .wave-field {
    left: 0; top: 0; width: 726px; height: 260px;
    background: radial-gradient(ellipse at 20% 30%, var(--wave-tone), transparent 70%);
  }

  .brand {
    position: absolute;
    left: 0; right: 0;
    display: flex; align-items: center; justify-content: center; gap: 14px;
    color: var(--logo-grey);
    font-weight: 700;
    font-size: 46px;
    line-height: 1.2;
    letter-spacing: 2px;
  }
  .brand__square { width: 22px; height: 22px; background: var(--accent-red); }
  .card--front .brand { top: 168px; }
  .card--back .brand  { top: 80px; }

  .motto {
    position: absolute; left: 0; right: 0; top: 336px;
    text-align: center;
    color: var(--text-grey);
    font-size: 20px;
  }
  .motto__divider { color: var(--accent-red); }

  .contact {
    position: absolute;
    transform: translateX(-50%);
    white-space: nowrap;
    color: var(--text-grey);
    font-size: 20px;
    text-align: center;
    padding: 0 4px 10px;
  }
  .contact::after {
    content: "";
    position: absolute; left: 0; right: 0; bottom: 0; height: 8px;
    border-left: 1px solid var(--rule);
    border-right: 1px solid var(--rule);
    background: linear-gradient(var(--rule), var(--rule)) center / 100% 1px no-repeat;
  }
  .contact--phone { left: 231px; top: 220px; }
  .contact--email { left: 509px; top: 220px; }
  .contact--web   { left: 368px; top: 302px; }
</style>
</head>
<body>
<main class="canvas">
  <section class="card card--front" aria-label="Card front">
    <div class="wave-field" role="img" aria-label="Fine flowing line pattern"></div>
    <div class="brand"><span class="brand__square"></span><span>Q7R Services</span></div>
    <p class="motto">Design <span class="motto__divider">||</span> Document <span class="motto__divider">||</span> Develop <span class="motto__divider">||</span> Deliver</p>
  </section>

  <section class="card card--back" aria-label="Card back">
    <div class="wave-field" role="img" aria-label="Fine flowing line pattern"></div>
    <div class="brand"><span class="brand__square"></span><span>Q7R Services</span></div>
    <p class="contact contact--phone">(+61) 400512836</p>
    <p class="contact contact--email">info@Q7RServices.example</p>
    <p class="contact contact--web">www.Q7RServices.example</p>
  </section>
</main>
</body>
</html>
```